lotus bowl vietnamese restaurant in need of a new menu

a family owned vietnamese restaurant in need of a new menu design that is fun, classy, and yet simple. menu that will catch the customers eyes. easy to read yet flows nicely. like to use the color green (basil green color) creme yellow and maroon. open to other colors as long as it looks nice together. our restaurant is family oriented, casual yet has a nice ambiance atmosphere.
prefer 11x17 portrait double sided. attached is our menu with the current price updated so use the info on this to start creating! looking for something unique, professional and one of a kind menu!
please use your own creative layout and design. we are open to ideas. the files uploaded are the updated prices and the logo is to use whichever one you feel goes with the menu.
Reason: don't see anything we like so far...please be creative!
Target Market(s)
restaurant consumers
Industry/Entity Type
Restaurant
Look and feel

```html
<!DOCTYPE html>
<html lang="en">
<head>
<meta charset="utf-8">
<title>Lotus Bowl Menu</title>
<link href="https://fonts.googleapis.com/css2?family=Oswald:wght@500;600&family=Roboto+Condensed:ital,wght@0,700;1,400;1,700&display=swap" rel="stylesheet">
<style>
:root{
  --cream:#fbf8c8;
  --cream-deep:#eee78a;
  --basil:#7cba2a;
  --basil-light:#c8e36e;
  --maroon:#3a1709;
  --maroon-mid:#6a361a;
  --gold:#d9b14a;
  --gold-light:#fbeaa5;
  --ink:#2f1a0c;
  --paper:#ffffff;
}
*{box-sizing:border-box;margin:0;padding:0}
html,body{width:1200px;height:783px;overflow:hidden;background:#fff}
.menu{position:relative;width:1200px;height:783px;font-family:'Roboto Condensed',sans-serif;color:var(--ink)}
.panel{position:absolute;overflow:hidden;padding:0 12px}
.panel--cream{background:radial-gradient(ellipse at 55% 45%,#fffde6 0%,var(--cream) 45%,var(--cream-deep) 100%)}
.panel--basil{background:radial-gradient(ellipse at 50% 50%,#e6f2a3 0%,var(--basil-light) 45%,var(--basil) 100%)}
.panel--maroon{background:radial-gradient(ellipse at 50% 40%,var(--maroon-mid) 0%,#4a2210 55%,var(--maroon) 100%);color:var(--paper)}
.banner{height:23px;margin:11px -12px 6px;background:linear-gradient(90deg,rgba(90,50,10,.0) 0%,#8a5a18 8%,var(--gold) 22%,var(--gold-light) 50%,var(--gold) 78%,#8a5a18 92%,rgba(90,50,10,0) 100%);text-align:center;border-top:1px solid #f6e3a0;border-bottom:1px solid #8a6420}
.banner h2{font-family:'Oswald',sans-serif;font-weight:600;font-size:16px;line-height:23px;color:var(--maroon);letter-spacing:.5px}
.sub{font-weight:700;font-style:italic;font-size:7.6px;text-align:center;text-transform:uppercase;margin:-2px 0 5px;line-height:1.25}
.item{margin-bottom:4px;line-height:1.12;text-transform:uppercase}
.item b{display:block;font-weight:700;font-size:8.4px}
.item i{display:block;font-size:7px}
.item.tight{margin-bottom:2px}
.note{font-size:7px;font-style:italic;text-transform:uppercase;line-height:1.15;margin-bottom:3px}
.note b{font-style:normal;font-size:8.4px}
.photo{position:absolute}
.oval{border-radius:50%;border:2px solid #2a1808;width:92px;height:58px}
.extras{position:absolute;left:399px;top:305px;width:399px;height:132px}
.extras ul{position:absolute;list-style:none;font-size:7.4px;text-transform:uppercase;color:var(--paper);line-height:1.3}
.flame{display:inline-block;width:7px;height:9px;vertical-align:-1px}
</style>
</head>
<body>
<div class="menu">

  <!-- Left column -->
  <section class="panel panel--cream" style="left:0;top:0;width:399px;height:443px">
    <div class="banner"><h2>APPETIZERS</h2></div>
    <div style="width:285px">
      <p class="note"><b>SPRING ROLLS (2)</b> comes with lettuce, vermicelli noodles rolled in rice paper served with peanut sauce with choice of: (cannot be mixed):</p>
      <div class="item"><b>1. Goi Cuon Tom &amp; Thit Heo | 4.50</b><i>Shrimp &amp; pork spring rolls</i></div>
      <div class="item"><b>2. Goi Cuon Thit Heo / Ga / or Bo Nuong | 5.50</b><i>Choice of: grilled pork / grilled chicken or grilled beef spring rolls</i></div>
      <div class="item"><b>3. Bi Cuon | 4.50</b><i>Pork skin roasted with rice powder spring rolls</i></div>
      <div class="item"><b>4. Cha Gio (2) | 4.50</b><i>Fried eggrolls with shrimp, pork &amp; vegetables rolled in egg wrap</i></div>
      <div class="item"><b>5. Canh Ga Nuoc Mam (6) | 7.95</b><i>Fried chicken wings</i></div>
      <div class="item"><b>6. Gio Tom (4) | 5.95</b><i>Fried shrimp rolls</i></div>
      <div class="item"><b>7. Ca Vien Chien (8) | 4.95</b><i>Fried fish balls</i></div>
      <div class="item"><b>8. Chao Tom (2) | 7.95</b><i>Grilled shrimp paste wrapped around sugar cane stick</i></div>
      <div class="item"><b>9. Wonton Soup (S) | 4.95 &nbsp;(L) 7.50</b><i>Wonton shrimp &amp; pork soup</i></div>
      <div class="item"><b>10. Tom Cua Soup (S) | 4.95 &nbsp;(L) 7.50</b><i>Crab meat, shrimp &amp; egg soup</i></div>
    </div>
    <p class="note"><b>VIETNAMESE SALAD</b> comes with thin cabbage, carrots, onions, mints, crushed peanuts tossed in lime juice &amp; vinegar with the following choices of:</p>
    <div class="item tight"><b>11. Goi Ga - Chicken Salad | 8.95</b></div>
    <div class="item"><b>12. Goi Tom - Shrimp Salad | 9.95</b></div>
    <div class="item"><b>13. Bo Tai Chanh | 11.95</b><i>Rare thin sliced beef with onions, mints, basils, crushed peanuts in lime juice &amp; vinegar</i></div>
    <div class="item"><b>14. Chim Cut Roti | 11.95</b><i>Roasted quails served with salt &amp; pepper</i></div>

    <div class="photo oval" style="left:290px;top:56px;background:radial-gradient(#f4d9c8,#cf8a78 60%,#8a9a5a)" role="img" aria-label="Photo of fresh spring rolls"></div>
    <div class="photo oval" style="left:288px;top:118px;background:radial-gradient(#f2cf7c,#c98a2a 65%,#6a4a20)" role="img" aria-label="Photo of fried eggrolls"></div>
    <div class="photo oval" style="left:290px;top:177px;background:radial-gradient(#e8b36a,#b8662a 65%,#5a3218)" role="img" aria-label="Photo of chicken wings"></div>
    <div class="photo oval" style="left:288px;top:232px;background:radial-gradient(#f0c86a,#c78a32 60%,#4a6a8a)" role="img" aria-label="Photo of fried shrimp rolls"></div>
    <div class="photo oval" style="left:290px;top:288px;background:radial-gradient(#eef0dc,#b8c89a 60%,#6a8a4a)" role="img" aria-label="Photo of vietnamese salad"></div>
  </section>

  <section class="panel panel--maroon" style="left:0;top:443px;width:399px;height:340px">
    <div class="banner"><h2>HU TIEU (MI) - NOODLE SOUP</h2></div>
    <p class="sub">Pork broth with rice or egg noodle</p>
    <div class="item"><b>15. Hu Tieu / Mi Dac Biet | 10.50</b><i>Choice of: rice or egg noodle with shrimp, roast pork, chicken, imitation crab, quail eggs, ground pork &amp; fried shrimp cracker combination noodle soup</i></div>
    <div class="item"><b>16. Hu Tieu / Mi Hai San | 11.50</b><i>Choice of: rice or egg noodle with shrimp, scallop, squid, fish balls &amp; imitation crab noodle soup</i></div>
    <div class="item"><b>17. Hu Tieu Mytho | 9.95</b><i>Shrimp, roast pork, chicken, fish ball, imitation crab &amp; ground pork with clear noodle soup</i></div>
    <div class="item"><b>18. Hu Tieu Sate | 9.50 <svg class="flame" viewBox="0 0 7 9"><path d="M3.5 0C5 2.5 7 4 6.5 6.5 6 8.5 1 8.5.5 6.5 0 4.5 2 4 2 2.5 3 3.5 3.5 2 3.5 0z" fill="#f07a1a"/></svg></b><i>Beef with tomato slices, cucumber, bean sprouts &amp; crushed peanuts in spicy noodle soup</i></div>
    <div class="item"><b>19. Hu Tieu / Mi Kho Dac Biet | 10.95</b><i>Choice of: rice or egg noodle with shrimp, roast pork, chicken, imitation crab, ground pork and fried shrimp cracker with soup on the side</i></div>
    <div class="item tight"><b>20. Mi Hoanh Thanh | 8.95</b><i>Wonton with egg noodle soup</i></div>
    <div class="item"><b>21. +Xa Xiu (Roast Pork) | 9.95</b></div>
    <div class="item"><b>22. Banh Canh Tom Thit Gio Heo | 9.50</b><i>Shrimp, pork knuckle &amp; vietnamese big noodle soup</i></div>
    <div class="item"><b>23. Banh Canh Ga | 8.95</b><i>Chicken with vietnamese big noodle soup</i></div>
  </section>

  <!-- Middle column -->
  <section class="panel panel--basil" style="left:399px;top:0;width:399px;height:443px">
    <div class="banner"><h2>PHO - RICE NOODLE SOUP</h2></div>
    <div class="item"><b>24. Pho Dac Biet | 9.50</b><i>Steak, brisket, flank, tendon, tripe &amp; meatballs combination noodle soup</i></div>
    <div class="item"><b>25. Pho | 8.50</b><i>Noodle soup with choices up to 3 items:<br>steak, brisket, flank, tendon, tripe, meatball or vegetables</i></div>
    <div class="item"><b>26. Pho Ga Vietnam (Ga Di Bo) | 10.50</b><i>Free range chicken noodle soup</i></div>
    <div class="item"><b>27. Pho Ga My | 9.50</b><i>White chicken &amp; mixed vegetables noodle soup</i></div>
    <div class="item"><b>28. Pho Thit Heo / Bo / or Ga Nuong | 10.50</b><i>Choice of: grilled pork, grilled beef or grilled chicken with mixed vegetables noodle soup</i></div>
    <div class="item"><b>29. Pho Do Bien | 11.50</b><i>Shrimp, scallop, squid, fish balls, imitation crab &amp; vegetables seafood noodle soup</i></div>
    <div class="item"><b>30. Pho Tom | 9.75</b><i>Shrimp with mixed vegetables noodle soup</i></div>
    <div class="item"><b>31. Pho Do Bien Chua Cay | 11.50</b><i>Shrimp, scallop, squid, fish balls &amp; imitation crab in hot &amp; sour noodle soup</i></div>
    <div class="item"><b>32. Pho Tre Em | 7.25</b><i>Kid's steak &amp; meatball noodle soup</i></div>
  </section>

  <div class="extras">
    <svg width="399" height="132" viewBox="0 0 399 132" style="position:absolute;left:0;top:0">
      <defs><radialGradient id="band" cx="50%" cy="50%" r="60%"><stop offset="0" stop-color="#7a4422"/><stop offset="1" stop-color="#3a1709"/></radialGradient></defs>
      <path d="M0 0H399V132H0Z" fill="#a9c85a"/>
      <path d="M0 8 Q20 8 30 22 L200 0 L369 22 Q379 8 399 8 V124 Q379 124 369 110 L200 132 L30 110 Q20 124 0 124Z" fill="url(#band)"/>
    </svg>
    <ul style="left:20px;top:34px">
      <li>* X-Large | 2.00 more</li>
      <li>* Extra meat (steak, chicken, etc..) | 3.50</li>
      <li>* Extra shrimp | 3.00</li>
      <li>* Extra herbs or vegetables | 1.50</li>
      <li>&nbsp;&nbsp;(ex: onions, culantros, basils, beansprouts, etc..)</li>
    </ul>
    <ul style="left:205px;top:34px">
      <li>* Extra rice, soup or noodles | 1.50</li>
      <li>* Change noodle or brown rice | 2.00</li>
      <li>* Add fried egg | 1.50</li>
      <li>* Add or change to fried rice | 3.00</li>
      <li>* Add eggroll | 2.25</li>
    </ul>
  </div>

  <section class="panel panel--cream" style="left:399px;top:437px;width:399px;height:346px">
    <div class="banner"><h2>BUN - VERMICELLI NOODLE BOWL</h2></div>
    <p class="sub">All vermicelli bowl comes with fresh lettuce, bean sprouts,<br>sliced cucumbers, shredded carrots &amp; crushed peanuts</p>
    <div style="width:250px">
      <div class="item"><b>33. Bun Dac Biet | 12.95</b><i>Choice of: grilled pork, grilled chicken or grilled beef with grilled shrimp &amp; fried eggroll special combination vermicelli bowl</i></div>
      <div class="item tight"><b>34. Bun - Vermicelli Bowl | 9.50</b><i>Choice of: grilled pork, grilled chicken or grilled beef</i></div>
      <div class="item tight"><b>35. + Eggroll | 9.95</b></div>
      <div class="item"><b>36. + Shrimp | 10.50</b></div>
      <div class="item"><b>37. Bun Tom Nuong (8) | 10.95</b><i>Grilled shrimp with vermicelli noodle bowl</i></div>
      <div class="item"><b>38. Bun Cha Gio (3) | 9.50</b><i>Fried eggroll vermicelli bowl</i></div>
      <div class="item"><b>39. Bun Chao Tom (2) | 9.50</b><i>Grilled shrimp paste vermicelli bowl</i></div>
    </div>
    <div class="item"><b>* 40. Bun Bo Hue | 9.50 <svg class="flame" viewBox="0 0 7 9"><path d="M3.5 0C5 2.5 7 4 6.5 6.5 6 8.5 1 8.5.5 6.5 0 4.5 2 4 2 2.5 3 3.5 3.5 2 3.5 0z" fill="#f07a1a"/></svg></b><i>Spicy beef noodle soup with beef shank, pork knuckle, pork blood with large vermicelli noodles</i></div>
    <div class="item"><b>* 41. Bun Rieu | 9.50</b><i>Mixed ground pork &amp; crab, pork blood, dried tofu with vermicelli rice noodle in tomato broth soup</i></div>
    <div class="item"><b>* 42. Bun Mang Vit | 9.50</b><i>Duck &amp; bamboo vermicelli noodle soup</i></div>
    <svg class="photo" style="left:218px;top:82px" width="168" height="128" viewBox="0 0 168 128" role="img" aria-label="Photo of a grilled meat vermicelli bowl">
      <defs><radialGradient id="bowl"><stop offset="0" stop-color="#e6b46a"/><stop offset=".6" stop-color="#a8642a"/><stop offset="1" stop-color="#4a6a2a"/></radialGradient></defs>
      <polygon points="84,0 100,22 130,8 126,38 166,44 136,64 166,88 126,90 130,122 100,104 84,128 68,104 38,122 42,90 2,88 32,64 2,44 42,38 38,8 68,22" fill="url(#bowl)" stroke="#3a1709" stroke-width="2"/>
    </svg>
  </section>

  <!-- Right column -->
  <section class="panel panel--maroon" style="left:798px;top:0;width:402px;height:240px">
    <div class="banner" style="margin-top:23px"><h2>COM TAM - BROKEN RICE PLATE</h2></div>
    <div style="padding-left:8px;margin-top:14px">
      <div class="item"><b>43. Com Dac Biet | 14.95</b><i>Special rice combination with grilled chicken, grilled pork, grilled shrimp &amp; fried eggroll</i></div>
      <div class="item"><b>44. Com Suon Nuong Xa | 9.95</b><i>Grilled pork chops marinated in lemongrass</i></div>
      <div class="item"><b>45. Com Suon Bi Cha | 9.50</b><i>Grilled pork chop, pork skin roasted with rice powder &amp; eggcake</i></div>
      <div class="item tight"><b>46. Com Thit Nuong, Ga Nuong or Bo Nuong | 9.75</b><i>Choice of: grilled pork, grilled chicken or grilled beef</i></div>
      <div class="item"><b>47. + Shrimp | 10.95</b></div>
      <div class="item"><b>48. Com Suon Dai Han | 13.95</b><i>Grilled korean bbq ribs</i></div>
    </div>
  </section>

  <section class="panel panel--cream" style="left:798px;top:240px;width:402px;height:203px">
    <div class="banner" style="margin-top:2px"><h2>COM CHIEN - FRIED RICE</h2></div>
    <p class="sub">Fried rice is cooked with egg, peas &amp; carrots</p>
    <div style="padding-left:8px;width:260px">
      <div class="item"><b>49. Com Chien Thap Cam | 10.95</b><i>House special fried rice with shrimp, roasted pork, sausage with peas &amp; carrots</i></div>
      <div class="item"><b>50. Com Chien Tom | 9.95</b><i>Shrimp fried rice</i></div>
      <div class="item"><b>51. Com Chien Ga | 9.95</b><i>Choice of: chicken fried rice</i></div>
      <div class="item"><b>52. Com Chien Canh Ga | 9.50</b><i>Fried rice with fried chicken wings</i></div>
      <div class="item tight"><b>53. Com Chien Bo Luc Lac | 14.50</b><i>Stir fry (shaking beef) filet mignon with bell peppers with fried rice</i></div>
      <div class="item"><b>54. + Shrimps | 16.95</b></div>
    </div>
    <div class="photo" style="left:242px;top:62px;width:122px;height:122px;border-radius:50%;border:2px solid #3a1709;background:radial-gradient(#f4d49a,#d9904a 55%,#7aa03a)" role="img" aria-label="Photo of a fried rice plate"></div>
  </section>

  <section class="panel panel--basil" style="left:798px;top:443px;width:402px;height:340px">
    <div class="banner" style="margin-top:0"><h2>XAO - STIR FRIED WITH RICE PLATE</h2></div>
    <div style="padding-left:8px;margin-top:14px">
      <div class="item"><b>55. Ga Xao Gung | 9.95</b><i>Stir fry chicken with ginger</i></div>
      <div class="item"><b>56. Ga or Bo Xao Xa Ot | 9.95</b><i>Choice of: stir fry chicken or beef in hot chili &amp; lemongrass</i></div>
      <div class="item"><b>57. Tom Xao Xa Ot | 10.95</b><i>Stir fry shrimp in hot chilli &amp; lemongrass</i></div>
      <div class="item"><b>58. Mi Xao Mem or Don Hai San | 14.95</b><i>Choice of: soft or crispy noodles stir fry with shrimp, squid, fish ball &amp; imitation crab with vegetables</i></div>
      <div class="item"><b>59. Ga or Bo Xao Rau Cai | 9.95</b><i>Stir fry chicken or beef with mixed vegetables</i></div>
      <div class="item"><b>60. Tom Xao Rau Cai | 10.95</b><i>Stir fry shrimp with mixed vegetables</i></div>
      <div class="item"><b>61. Com Tom Rang Chay Mo | 10.95</b><i>Stir fry shrimp, ginger, onion &amp; bell pepper in garlic sauce</i></div>
      <div class="item"><b>* 62. Canh Chua Ca or Tom | 14.95</b><i>Choice of: fish or shrimp soup with tomato, pineapple, okra &amp; bean sprouts served with white rice (serving 2-4)</i></div>
      <div class="item"><b>* 63. Ca Kho To | 14.95</b><i>Braised swai fish in clay pot with black pepper &amp; dry shallots served with white rice</i></div>
    </div>
  </section>

</div>
</body>
</html>
```